Travel video blogger needs website design

I need a website designed for my new travel video blog "Roaming Compass". I have only just started but need a website that is fairly simple and not too busy. I have a logo which I want on it (I have attached it to this project). I also want a link to all my other social medias on the main page (vidstreamhub, Snapmosaic and friendweave) and my videos as well. Here is a link to my vidstreamhub page for you to look at: https://www.vidstreamhub.example/channel/QXr7mPzT2wVn84KsdYe31jaB
As I have only just started and I am still trying to find my specific niche, again I need it to be sleek and simple that I can go in and change slightly here and there. I would like these pages on the website: About Me, Videos, Social Media, Blog, Gallery, contact me. for an example I like the look of www.wanderingkinfolk.example website.

I already have the domain and I am with Nestwarp with wordpress.org. I just want to spend my time getting better and learning about videos then trying to create a website (I am a bit of a perfectionist when I try to do something).

I

Target Market(s)

Young Adults (majority females) between the ages of 18 and 30 with an interest in travelling.

Industry/Entity Type

Travel Industry

Number of Pages Required

1 page

Colors

Designer to choose colors to be used in the design.

Requirements
Must have
• A like to my Snapmosaic, friendweave and vidstreamhub channels on the home page
• Must be a nice, simple design
• Must have my logo on the front and name "Roaming Compass"
Nice to have
• A nice light, bright coloured theme
Should not have
• A dark coloured theme

```html
<!DOCTYPE html>
<html lang="en">
<head>
<meta charset="utf-8">
<title>Roaming Compass – Travel the world with me</title>
<link href="https://fonts.googleapis.com/css2?family=Raleway:wght@300;400;500;600;700&family=Great+Vibes&family=Roboto:wght@300;400;500;700&display=swap" rel="stylesheet">
<style>
:root{
  --sand:#e2b986;
  --sand-dark:#c99a5e;
  --cream:#faf3ec;
  --ink:#2c2c2c;
  --muted:#8a8a8a;
  --white:#ffffff;
  --map:#ececec;
  --footer:#3a3c47;
  --footer-deep:#23242b;
  --hero-top:#4a4f55;
  --hero-mid:#2f3b3f;
  --hero-sea:#253846;
}
*{margin:0;padding:0;box-sizing:border-box}
html,body{width:1200px;height:3622px;overflow:hidden}
body{position:relative;font-family:'Raleway',sans-serif;color:var(--ink);background:var(--white)}
a{color:inherit;text-decoration:none}

/* Hero */
.hero{position:absolute;left:0;top:0;width:1200px;height:801px;overflow:hidden}
.hero-photo{position:absolute;inset:0;background:linear-gradient(180deg,var(--hero-top) 0%,#3a4146 30%,var(--hero-mid) 55%,var(--hero-sea) 80%,#1e2a33 100%)}
.brand{position:absolute;left:65px;top:-66px;width:218px;height:218px;border-radius:50%;background:var(--sand);display:flex;align-items:flex-end;justify-content:center;padding-bottom:42px}
.brand-name{font-family:'Raleway',sans-serif;font-weight:600;font-size:19px;letter-spacing:1px;color:var(--white);text-transform:uppercase}
.follow{position:absolute;left:797px;top:0;width:265px;height:34px;background:#1c1c1c;clip-path:polygon(0 0,100% 0,92% 100%,8% 100%);display:flex;align-items:center;justify-content:center;gap:10px;font-family:'Roboto',sans-serif;font-size:12px;font-weight:700;color:var(--sand);letter-spacing:1px}
.follow .dot{width:10px;height:10px;border-radius:50%;background:var(--white)}
.nav{position:absolute;top:52px;left:545px;display:flex;font-family:'Raleway',sans-serif;font-size:14px;font-weight:600;color:var(--white)}
.nav li{list-style:none;margin-right:26px}
.nav li.active{border-bottom:2px solid var(--white);padding-bottom:3px}
.nav .caret{font-size:9px;margin-left:3px}
.hero-kicker{position:absolute;left:261px;top:326px;font-size:24px;font-style:italic;font-weight:400;color:#f3e4cf}
.hero-title{position:absolute;left:255px;top:350px;font-family:'Great Vibes',cursive;font-size:92px;font-weight:400;color:var(--sand);line-height:1}
.slider-dots{position:absolute;top:734px;left:576px;display:flex;gap:10px}
.slider-dots span{width:9px;height:9px;border-radius:50%;border:1.5px solid var(--white)}
.slider-dots span.on{background:var(--white)}

/* Gallery */
.gallery{position:absolute;left:0;top:801px;width:1200px;height:708px;background:var(--cream)}
.section-title{display:flex;align-items:center;gap:14px;font-size:28px;font-weight:500;letter-spacing:1px;text-transform:uppercase}
.section-title .mark{width:46px;height:46px;border-radius:50%;border:2.5px solid var(--ink)}
.section-title em{font-style:normal;color:var(--sand)}
.gallery .section-title{position:absolute;top:66px;left:426px}
.place{position:absolute;top:180px;width:262px;text-align:center}
.place .photo{width:232px;height:232px;border-radius:50%;margin:0 auto;border:4px solid var(--white);box-shadow:0 2px 6px rgba(0,0,0,.12)}
.place h3{margin-top:26px;font-size:24px;font-weight:500;color:var(--sand)}
.place p{margin-top:10px;font-family:'Roboto',sans-serif;font-size:12.5px;line-height:1.5;color:var(--muted);padding:0 20px}
.btn-sand{position:absolute;left:519px;top:592px;width:164px;height:36px;background:var(--sand);color:var(--white);font-family:'Roboto',sans-serif;font-size:15px;display:flex;align-items:center;justify-content:center}

/* Traveller band */
.traveller{position:absolute;left:0;top:1509px;width:1200px;height:476px;background:linear-gradient(90deg,var(--sand) 0%,#e6c59a 38%,#c9b08e 55%,#8f8a82 75%,#5a5e63 100%)}
.traveller-photo{position:absolute;right:0;top:0;width:560px;height:476px;background:linear-gradient(180deg,#c8c0b6 0%,#d8b58a 45%,#9c8670 75%,#4d4a48 100%);opacity:.85}
.traveller-quote{position:absolute;left:145px;top:130px;font-family:'Great Vibes',cursive;font-size:40px;line-height:53px;color:var(--ink)}
.socials-line{position:absolute;left:145px;top:330px;display:flex;gap:12px}
.socials-line a{height:40px;padding:0 14px;border:2px solid var(--ink);border-radius:20px;display:flex;align-items:center;font-size:13px;font-weight:600;color:var(--ink)}

/* Map */
.map{position:absolute;left:0;top:1985px;width:1200px;height:663px;background:var(--map)}
.pin{position:absolute;width:26px;height:34px}
.map-card{position:absolute;left:478px;top:168px;width:241px;background:var(--white);box-shadow:0 3px 10px rgba(0,0,0,.15);padding-bottom:16px}
.map-card .photo{height:150px;background:linear-gradient(180deg,#7fb5d8 0%,#8fc08a 50%,#d8c9a5 100%)}
.map-card h4{margin:18px 20px 0;font-family:'Roboto',sans-serif;font-size:14px;font-weight:500;color:var(--ink)}
.map-card p{margin:10px 20px 0;font-family:'Roboto',sans-serif;font-size:11.5px;line-height:1.45;color:var(--muted)}

/* Passion band */
.passion{position:absolute;left:0;top:2648px;width:1200px;height:278px;background:var(--sand);text-align:center}
.passion h2{position:absolute;top:82px;width:100%;font-family:'Roboto',sans-serif;font-size:24px;font-weight:300;letter-spacing:.5px;color:var(--white);text-transform:uppercase}
.passion h2 strong{font-weight:700}
.btn-outline{position:absolute;left:490px;top:147px;width:217px;height:51px;border:2px solid var(--white);color:var(--white);font-family:'Roboto',sans-serif;font-size:15px;display:flex;align-items:center;justify-content:center}

/* About */
.about{position:absolute;left:0;top:2926px;width:1200px;height:442px;background:var(--white)}
.about .section-title{position:absolute;left:126px;top:86px;font-size:26px}
.about-text{position:absolute;left:150px;top:190px;width:440px;font-family:'Roboto',sans-serif;font-size:13px;line-height:1.9;color:#555}
.about-text p+p{margin-top:22px}
.video{position:absolute;left:620px;top:79px;width:430px;height:273px;background:#111}
.video .still{position:absolute;left:0;top:31px;width:430px;height:210px;background:linear-gradient(100deg,#b9a18a 0%,#d9c6b0 45%,#e6c9a4 70%,#c69c77 100%)}
.video .play{position:absolute;left:188px;top:118px;width:54px;height:36px}

/* Footer */
.footer{position:absolute;left:0;top:3368px;width:1200px;height:176px;background:var(--footer);color:var(--white);font-family:'Roboto',sans-serif}
.fcol{position:absolute;top:42px}
.fcol h5{font-size:18px;font-weight:500;text-transform:uppercase}
.fcol .sub{font-size:14px;color:#ddd;margin-top:1px}
.fcol .line{font-size:15px;margin-top:26px}
.fcol .mail{text-decoration:underline;margin-top:8px;display:block;font-size:15px}
.ficons{display:flex;gap:10px;margin-top:20px;font-size:11px;font-weight:500}
.newsletter-form{display:flex;margin-top:18px}
.newsletter-form .input{width:179px;height:32px;background:var(--white);color:#555;font-size:12px;display:flex;align-items:center;padding-left:8px}
.newsletter-form .submit{width:118px;height:32px;background:var(--sand);color:var(--white);font-size:13px;display:flex;align-items:center;justify-content:center;text-transform:uppercase}
.bottom{position:absolute;left:0;top:3544px;width:1200px;height:78px;background:var(--footer-deep);color:#bbb;font-family:'Roboto',sans-serif;font-size:12px;display:flex;align-items:center;justify-content:center}
</style>
</head>
<body>

<header class="hero">
  <div class="hero-photo" role="img" aria-label="Photo of a traveller paddling a yellow kayak towards green limestone cliffs on calm water"></div>
  <div class="brand"><span class="brand-name">Roaming Compass</span></div>
  <div class="follow">FOLLOW US : <span class="dot"></span><span class="dot"></span><span class="dot"></span><span class="dot"></span><span class="dot"></span></div>
  <ul class="nav">
    <li class="active">Home</li>
    <li>About Me<span class="caret">▾</span></li>
    <li>Videos<span class="caret">▾</span></li>
    <li>Social Media<span class="caret">▾</span></li>
    <li>Blog<span class="caret">▾</span></li>
    <li>Gallery<span class="caret">▾</span></li>
    <li>Contact</li>
  </ul>
  <p class="hero-kicker">Welcome to Roaming Compass</p>
  <h1 class="hero-title">Travel the world with me</h1>
  <div class="slider-dots"><span class="on"></span><span></span><span></span></div>
</header>

<section class="gallery">
  <h2 class="section-title"><span class="mark"></span><span>Our <em>Gallery</em></span></h2>
  <div class="place" style="left:79px">
    <div class="photo" role="img" aria-label="Photo of a decorated camel resting in the desert" style="background:linear-gradient(160deg,#d99b62,#b5542f 55%,#6b3a26)"></div>
    <h3>Dubai</h3>
    <p>Lorem ipsum dolor sit amet, enim detracto vulputate eum ad, discere eruditi alienum cu per. No case habeo has duo ne iusto quidam.</p>
  </div>
  <div class="place" style="left:340px">
    <div class="photo" role="img" aria-label="Photo of overwater huts below a green mountain and turquoise lagoon" style="background:linear-gradient(180deg,#5aa6e0,#3f8a4a 45%,#2fc0c6 75%,#1c9fb0)"></div>
    <h3>Switzerland</h3>
    <p>Lorem ipsum dolor sit amet, enim detracto vulputate eum ad, discere eruditi alienum cu per. No case habeo has duo ne iusto quidam.</p>
  </div>
  <div class="place" style="left:603px">
    <div class="photo" role="img" aria-label="Photo of a domed palace at sunset reflected in water" style="background:linear-gradient(180deg,#d95a80,#9a3f6a 50%,#3b2140)"></div>
    <h3>New Delhi</h3>
    <p>Lorem ipsum dolor sit amet, enim detracto vulputate eum ad, discere eruditi alienum cu per. No case habeo has duo ne iusto quidam volutpat.</p>
  </div>
  <div class="place" style="left:864px">
    <div class="photo" role="img" aria-label="Photo of stone statues in front of a city skyline and blue sky" style="background:linear-gradient(180deg,#4aa0e8,#9cc6e8 45%,#5b6c78 75%,#2d3a44)"></div>
    <h3>Bahamas</h3>
    <p>Lorem ipsum dolor sit amet, enim detracto vulputate eum ad, discere eruditi alienum cu per. No case habeo has duo ne iusto quidam.</p>
  </div>
  <a class="btn-sand" href="#">More photos</a>
</section>

<section class="traveller">
  <div class="traveller-photo" role="img" aria-label="Photo of a backpacker with arms raised on a cliff above the sea at sunset"></div>
  <p class="traveller-quote">I'm the traveller,<br>writer and person behind Roaming Compass!,<br>a travel blog!</p>
  <nav class="socials-line" aria-label="Social channels">
    <a href="#">friendweave</a>
    <a href="#">Snapmosaic</a>
    <a href="#">Pinboardly</a>
    <a href="#">Circlecast</a>
    <a href="#">vidstreamhub</a>
  </nav>
</section>

<section class="map" role="img" aria-label="Light grey world map showing countries and place names with visited locations pinned">
  <svg class="pin" style="left:197px;top:379px" viewBox="0 0 26 34"><path d="M13 33C13 33 2 19 2 12a11 11 0 0 1 22 0c0 7-11 21-11 21z" fill="#e2b986"/><circle cx="13" cy="12" r="4.5" fill="#fff"/></svg>
  <svg class="pin" style="left:376px;top:415px" viewBox="0 0 26 34"><path d="M13 33C13 33 2 19 2 12a11 11 0 0 1 22 0c0 7-11 21-11 21z" fill="#e2b986"/><circle cx="13" cy="12" r="4.5" fill="#fff"/></svg>
  <svg class="pin" style="left:448px;top:418px" viewBox="0 0 26 34"><path d="M13 33C13 33 2 19 2 12a11 11 0 0 1 22 0c0 7-11 21-11 21z" fill="#e2b986"/><circle cx="13" cy="12" r="4.5" fill="#fff"/></svg>
  <svg class="pin" style="left:484px;top:488px" viewBox="0 0 26 34"><path d="M13 33C13 33 2 19 2 12a11 11 0 0 1 22 0c0 7-11 21-11 21z" fill="#e2b986"/><circle cx="13" cy="12" r="4.5" fill="#fff"/></svg>
  <svg class="pin" style="left:542px;top:468px" viewBox="0 0 26 34"><path d="M13 33C13 33 2 19 2 12a11 11 0 0 1 22 0c0 7-11 21-11 21z" fill="#e2b986"/><circle cx="13" cy="12" r="4.5" fill="#fff"/></svg>
  <svg class="pin" style="left:361px;top:568px" viewBox="0 0 26 34"><path d="M13 33C13 33 2 19 2 12a11 11 0 0 1 22 0c0 7-11 21-11 21z" fill="#e2b986"/><circle cx="13" cy="12" r="4.5" fill="#fff"/></svg>
  <svg class="pin" style="left:733px;top:539px" viewBox="0 0 26 34"><path d="M13 33C13 33 2 19 2 12a11 11 0 0 1 22 0c0 7-11 21-11 21z" fill="#e2b986"/><circle cx="13" cy="12" r="4.5" fill="#fff"/></svg>
  <svg class="pin" style="left:856px;top:339px" viewBox="0 0 26 34"><path d="M13 33C13 33 2 19 2 12a11 11 0 0 1 22 0c0 7-11 21-11 21z" fill="#e2b986"/><circle cx="13" cy="12" r="4.5" fill="#fff"/></svg>
  <svg class="pin" style="left:1003px;top:530px" viewBox="0 0 26 34"><path d="M13 33C13 33 2 19 2 12a11 11 0 0 1 22 0c0 7-11 21-11 21z" fill="#e2b986"/><circle cx="13" cy="12" r="4.5" fill="#fff"/></svg>
  <article class="map-card">
    <div class="photo" role="img" aria-label="Photo of palm trees and huts on a tropical beach"></div>
    <h4>5 Reasons to visit this place</h4>
    <p>Lorem ipsum dolor sit amet, enim detracto vulputate eum ad, discere eruditi alienum cu per. No case habeo has, duo ne iusto quidam volutpat. Cu iusto ignota has, eum aperiam.</p>
  </article>
</section>

<section class="passion">
  <h2>Travelling is my biggest passion <strong>your journey begins with me</strong></h2>
  <a class="btn-outline" href="#">Follow my daily updates</a>
</section>

<section class="about">
  <h2 class="section-title"><span class="mark"></span><span><em>About</em> Me</span></h2>
  <div class="about-text">
    <p>Welcome to my family here at Roaming Compass! My name is Maren, I am 23 years old and next year I have decided to travel the world. Follow me as I travel around the world.</p>
    <p>Lorem ipsum dolor sit amet, enim detracto vulputate eum ad, discere eruditi alienum cu per. No case habeo has, duo ne iusto quidam volutpat. Cu iusto ignota has, eum aperiam.</p>
  </div>
  <div class="video">
    <div class="still" role="img" aria-label="Video still of a smiling traveller on a sandy beach"></div>
    <svg class="play" viewBox="0 0 54 36"><rect width="54" height="36" rx="6" fill="#222"/><path d="M22 11l12 7-12 7z" fill="#fff"/></svg>
  </div>
</section>

<footer class="footer">
  <div class="fcol" style="left:94px">
    <h5>Contact Me</h5>
    <p class="line">+1 800 555 0147</p>
    <a class="mail" href="#">name@roamingcompass.example</a>
  </div>
  <div class="fcol" style="left:435px">
    <h5>Connect With Us</h5>
    <p class="sub">Social Media Channels</p>
    <div class="ficons"><span>friendweave</span><span>Snapmosaic</span><span>vidstreamhub</span></div>
  </div>
  <div class="fcol" style="left:765px">
    <h5>Newsletter</h5>
    <p class="sub">Signup for a special offers</p>
    <div class="newsletter-form"><span class="input">Email</span><span class="submit">Subscribe</span></div>
  </div>
</footer>
<div class="bottom">© 2018 roamingcompass All Right Reserved</div>

</body>
</html>
```